Web Design Project: Facility Management company

Hi! We need a new website.

Our current website: http://www.vireo-trade.ru/ and we don-t like it. =)
The structure of our company has changed and now we don't need "cleaning" and "engeneering" on this site.

We are facility management company in Russia. So we provide integrated service solutions specific to industrial services: maintenance, repair, etc. of engineering systems.
More services:
Energy planning
Automation
Audit
Statements with regulators
Video surveillance
Central heating
Security systems
Welding
Management of subcontractors
Electrical installation and service needs
Reception
Catering

Visitors:
* Managers in the field of commercial real estate
* Chief engineers
* TOP managers of large companies, malls, factories...
+ their subordinates
* Small% of applicants.

Here you can see some websites/patterns we liked:
http://www.kobalmire.ru/ (This is our competitor’s site, so our site shouldn’t be an exact copy))))
http://www.dwatqo.ru/
http://www.layoutfarrow.com/demo/24296.html
http://www.layoutfarrow.com/website-templates/10145.html

Style:
Light, hi-tech/minimalizm, the color palette should be based on the original site colors (Green + black + white). http://www.vireo-trade.ru/

Estimated sitemap:
1. Home
2. About Us
3. Company's policy
4. History + Achievements.
5. Certificates
6. Map of presence (Here you can use sample map in file "our projects")
7. Services
8. Portfolio
9. News or blog
10. Jobs
11. Contacts - with the feedback form (or the function "call to order")
12. English

Need a design pages: main page, page 404. The rest of the page could be created by general pattern.

Logo, navigation bar and contacts should be visible on all pages of a site.
Flash animation elements and buttons, etc. - not needed.

* We need to develop 3 websites, so we are looking for a long term cooperation.
Looking forward to your creativity =)

Must Have:
Clear, intuitive structure of web pages.
In the center - of pictures reflecting our main services (industrial theme). May be in rotation.
BUT! This banner (central picture) should not be a huge one =)
All relevant information should be visible at once without scrolling.

A possibility to place media files (presentations, video ...) and 2 banner links on the main page.

Font should be available in Cyrillic.
Updates

IMPORTANT!

Please notice that in thisdesign we don't need "cleaning" and "engeneering" on this site.

So don't use old block of 4pictures from our current website. We don't need it anymore. 

Thestructure of our company has changed and now we need some links (may be banners,may be something else) to our future cleaning website as well as engeneeringwebsite.
It should look like seperate (partner) companies, not like our sevices.

Regards, Vera.

Please don't forget that we need bilingual site.

So define language changing tool in your designs.

Industry/Entity Type

Industrial

```html
<!DOCTYPE html>
<html lang="en">
<head>
<meta charset="utf-8">
<title>Aldermont — Facility Management</title>
<link href="https://fonts.googleapis.com/css2?family=Didact+Gothic&family=PT+Sans:wght@400;700&display=swap" rel="stylesheet">
<style>
  :root {
    --lime: #d6e58a;
    --lime-bright: #a8dc5a;
    --ink: #222222;
    --charcoal: #333333;
    --night: #111111;
    --field: #8c8c8c;
    --paper: #ffffff;
    --mist: #ebebeb;
    --icon: #bdbdbd;
  }
  * { margin: 0; padding: 0; box-sizing: border-box; }
  html, body { width: 960px; height: 1200px; overflow: hidden; }
  body { position: relative; background: var(--paper); font-family: "PT Sans", Arial, sans-serif; color: var(--ink); }
  .abs { position: absolute; }
  .display { font-family: "Didact Gothic", "PT Sans", sans-serif; }

  /* header */
  .site-header { left: 0; top: 0; width: 960px; height: 150px; background: var(--paper); }
  .brand { left: 93px; top: 74px; display: flex; align-items: center; gap: 12px; }
  .brand-mark { width: 22px; height: 22px; background: var(--lime-bright); }
  .brand-name { font-family: "Didact Gothic", sans-serif; font-size: 30px; letter-spacing: 7px; color: var(--ink); }
  .social { top: 33px; width: 26px; height: 26px; border-radius: 50%; background: var(--icon); }
  .phone { right: 114px; top: 60px; font-size: 14px; color: #444; }
  .lang-switch { left: 783px; top: 83px; width: 62px; height: 19px; background: var(--lime); font-size: 13px; color: #444; text-align: center; line-height: 19px; }
  .main-nav { left: 431px; top: 113px; width: 415px; display: flex; justify-content: space-between; font-size: 13px; color: var(--ink); }

  /* hero */
  .hero-band { left: 0; top: 150px; width: 960px; height: 276px; background: var(--lime); }
  .hero-photo { left: 94px; top: 150px; width: 752px; height: 276px; background: linear-gradient(180deg, #3f78d8 0%, #8fb4e8 40%, #d9cfc2 62%, #6e7b5a 100%); }
  .hero-caption { left: 97px; top: 282px; width: 410px; height: 94px; background: rgba(60,60,60,0.72); }
  .hero-title { left: 108px; top: 293px; font-size: 20.5px; line-height: 20px; color: var(--paper); font-weight: 400; }
  .btn { background: var(--lime); color: var(--charcoal); font-weight: 700; font-size: 13px; text-align: center; }
  .hero-btn { left: 110px; top: 346px; width: 88px; height: 21px; line-height: 21px; }

  /* content */
  .content-bg { left: 0; top: 426px; width: 960px; height: 432px; background: var(--mist); }
  .dot { top: 449px; width: 10px; height: 10px; border-radius: 50%; background: var(--charcoal); }
  .dot.active { background: var(--paper); border: 1.5px solid var(--charcoal); }

  .quick-links { left: 94px; top: 481px; width: 240px; height: 145px; background: var(--lime); padding: 13px 0 0 12px; }
  .quick-links li { list-style: none; font-family: "Didact Gothic", sans-serif; font-size: 15.5px; height: 24.5px; display: flex; align-items: center; gap: 9px; color: var(--ink); }
  .quick-links li::before { content: ""; width: 0; height: 0; border-left: 6px solid var(--charcoal); border-bottom: 5px solid transparent; }

  .other-services { left: 94px; top: 639px; width: 240px; height: 193px; background: var(--charcoal); color: var(--paper); }
  .card { top: 481px; width: 213px; height: 353px; background: var(--paper); }
  .card-image { width: 178px; height: 157px; }
  .block-title { font-family: "Didact Gothic", sans-serif; font-size: 15px; line-height: 14.5px; font-weight: 400; }
  .block-text { font-size: 10.5px; line-height: 12px; }
  .small-btn { width: 89px; height: 20px; line-height: 20px; }

  /* footer */
  .footer-panel { left: 0; top: 858px; width: 960px; height: 283px; background: var(--charcoal); color: var(--paper); }
  .footer-title { font-family: "Didact Gothic", sans-serif; font-size: 16.5px; color: var(--paper); font-weight: 400; }
  .field { background: var(--field); color: var(--paper); font-weight: 700; font-size: 12px; padding-left: 8px; display: flex; align-items: center; }
  .presence-map { left: 380px; top: 924px; width: 268px; height: 186px; background: radial-gradient(ellipse at 55% 50%, #a6e061 0%, #8fce4c 70%, #6fae38 100%); border-radius: 18px; }
  .bottom-bar { left: 0; top: 1141px; width: 960px; height: 59px; background: var(--night); display: flex; justify-content: center; align-items: center; }
  .bottom-bar a { color: var(--paper); text-decoration: none; font-size: 12.5px; padding: 0 9px; border-left: 1px solid #cfcfcf; line-height: 22px; }
  .bottom-bar a:first-child { border-left: none; }
</style>
</head>
<body>

<header class="abs site-header">
  <div class="abs brand"><span class="brand-mark"></span><span class="brand-name">ALDERMONT</span></div>
  <span class="abs social" style="left:741px"></span>
  <span class="abs social" style="left:781px"></span>
  <span class="abs social" style="left:820px"></span>
  <div class="abs phone">(02) 555-01987</div>
  <div class="abs lang-switch">Русский</div>
  <nav class="abs main-nav display">
    <span>HOME</span><span>ABOUT US</span><span>SERVICES</span><span>CERTIFICATES</span><span>BLOG</span><span>CONTACT</span>
  </nav>
</header>

<section>
  <div class="abs hero-band"></div>
  <div class="abs hero-photo" role="img" aria-label="Modern office building with glass windows under a blue sky"></div>
  <div class="abs hero-caption"></div>
  <h1 class="abs hero-title display">we provide integrated service solutions<br>specific to industrial services.</h1>
  <div class="abs btn hero-btn">Learn More</div>
</section>

<main>
  <div class="abs content-bg"></div>
  <span class="abs dot active" style="left:439px"></span>
  <span class="abs dot" style="left:455px"></span>
  <span class="abs dot" style="left:472px"></span>
  <span class="abs dot" style="left:489px"></span>

  <ul class="abs quick-links">
    <li>Company's policy</li>
    <li>History &amp; achievements</li>
    <li>Map of presence</li>
    <li>Portofolio</li>
    <li>Jobs</li>
  </ul>

  <div class="abs other-services">
    <h2 class="abs block-title" style="left:22px;top:20px">Other services</h2>
    <p class="abs block-text" style="left:24px;top:61px;width:178px">Lorem Ipsum is simply dummy text of the printing and typesetting industry. Lorem Ipsum has been the industry's standard dummy text ever since the 1500s, when an unknown printer took a galley of type and scrambled.</p>
    <div class="abs btn small-btn" style="left:25px;top:159px">Learn More</div>
  </div>

  <article class="abs card" style="left:363px">
    <div class="abs card-image" style="left:16px;top:13px;background:linear-gradient(160deg,#2f6fc4,#9cc4ee 50%,#3b7fd0)" role="img" aria-label="Glass skyscraper reflecting clouds"></div>
    <h2 class="abs block-title" style="left:17px;top:185px">Integrated facility<br>management</h2>
    <p class="abs block-text" style="left:19px;top:225px;width:176px">Lorem Ipsum is simply dummy text of the printing and typesetting industry. Lorem Ipsum has been the industry's standard dummy text ever since the 1500s, when an unknown printer took a galley of type and scrambled.</p>
    <div class="abs btn small-btn" style="left:20px;top:317px">Learn More</div>
  </article>

  <article class="abs card" style="left:620px">
    <div class="abs card-image" style="left:17px;top:13px;background:linear-gradient(135deg,#c9c9c9,#eeeeee 50%,#a9a9a9)" role="img" aria-label="White industrial pipes against a textured wall"></div>
    <h2 class="abs block-title" style="left:17px;top:185px">Technical maintenace of<br>engineering systems</h2>
    <p class="abs block-text" style="left:19px;top:224px;width:176px">Lorem Ipsum is simply dummy text of the printing and typesetting industry. Lorem Ipsum has been the industry's standard dummy text ever since the 1500s, when an unknown printer took a galley of type and scrambled.</p>
    <div class="abs btn small-btn" style="left:19px;top:317px">Learn More</div>
  </article>
</main>

<footer>
  <div class="abs footer-panel"></div>

  <h2 class="abs footer-title" style="left:93px;top:870px">Newsletter</h2>
  <p class="abs block-text" style="left:93px;top:910px;width:168px;color:var(--paper)">Sign up here to receive regular e-newsletter. Please note you will only be added to the list if a full name is submitted.</p>
  <div class="abs field" style="left:92px;top:967px;width:178px;height:28px">Email</div>
  <div class="abs field" style="left:92px;top:1003px;width:178px;height:28px">Name</div>
  <div class="abs btn small-btn" style="left:94px;top:1040px;height:21px;line-height:21px">Submit</div>

  <h2 class="abs footer-title" style="left:286px;top:870px">Map of presence</h2>
  <div class="abs btn small-btn" style="left:286px;top:897px;height:21px;line-height:21px">Learn More</div>
  <div class="abs presence-map" role="img" aria-label="Map of Russia marking company locations, including Saint Petersburg and Moscow"></div>

  <h2 class="abs footer-title" style="left:669px;top:871px">Contact Us</h2>
  <div class="abs field" style="left:670px;top:913px;width:175px;height:22px;padding-left:12px">Email</div>
  <div class="abs field" style="left:670px;top:941px;width:175px;height:22px;padding-left:12px">Tel</div>
  <div class="abs field" style="left:670px;top:970px;width:175px;height:23px;padding-left:12px">Subject</div>
  <div class="abs field" style="left:671px;top:1000px;width:175px;height:70px;padding-left:10px;align-items:flex-start;padding-top:6px">Contect</div>
  <div class="abs btn small-btn" style="left:671px;top:1078px;height:21px;line-height:21px">Submit</div>

  <nav class="abs bottom-bar display">
    <a href="#">HOME</a><a href="#">ABOUT US</a><a href="#">SERVICES</a><a href="#">CERTIFICATES</a><a href="#">BLOG</a><a href="#">CONTACT</a>
  </nav>
</footer>

</body>
</html>
```